Business Card and Letterhead Design for Public Accounting Firm

Business card and letterhead design for a CPA Firm located in Orange County, CA. We're looking for a modern and professional design utilizing our existing logo. We'd like a clean "less is more" look, but also something that catches the eye. We provide a high level of service to our clients. Open to single or double sided business cards.

Additional info: color numbers on logo
Blue :
R 0
G 83
B 125

#00537D

Silver :

R 154
G 154
B 154

#9A9A9A

Target Market(s)

Businesses and individuals

Industry/Entity Type

Accounting

Contact Information for Business Card

Moss Whitfield & Danby LLP - 4827 Larkspur Vale Road, Irvine, CA 92614 - (949)731-2864 - mwdaccts.example

Font styles to use
Serif
Sans Serif
Other font styles liked:
• See font file uploaded

Colors
0054AA
0677BA
7BADD7
CADEEF
E8F1F8

Requirements
Nice to have
• Possibly use the font file provided which matches our logo, but adjust to be not in all caps

```html
<!DOCTYPE html>
<html lang="en">
<head>
<meta charset="utf-8">
<title>Moss Whitfield &amp; Danby LLP — Business Card</title>
<link rel="stylesheet" href="https://fonts.googleapis.com/css2?family=Cinzel:wght@500&family=Tinos:wght@400;700&display=swap">
<style>
  :root {
    --stage: #2c2f33;
    --brand-blue: #0b5883;
    --brand-blue-deep: #044a72;
    --brand-silver: #9a9a9a;
    --paper: #ffffff;
    --ink-grey: #6b6b6b;
  }
  html, body {
    margin: 0;
    padding: 0;
    width: 1200px;
    height: 952px;
    overflow: hidden;
    background: var(--stage);
  }
  .canvas {
    position: relative;
    width: 1200px;
    height: 952px;
    display: flex;
    align-items: center;
    justify-content: center;
    gap: 48px;
  }
  .card {
    position: relative;
    width: 520px;
    height: 300px;
    border-radius: 22px;
    overflow: hidden;
    box-shadow: 0 14px 34px rgba(0,0,0,.45);
  }
  .card-bands {
    position: absolute;
    inset: 0;
    width: 100%;
    height: 100%;
  }

  /* Front side */
  .card-front { background: var(--brand-blue); }
  .front-identity {
    position: absolute;
    left: 70px;
    top: 80px;
    display: flex;
    align-items: center;
    gap: 18px;
    color: var(--paper);
  }
  .identity-rule {
    width: 1px;
    height: 78px;
    background: var(--paper);
  }
  .firm-name {
    font-family: "Cinzel", serif;
    font-weight: 500;
    font-size: 27px;
    line-height: 1.15;
    letter-spacing: 2px;
    margin: 0;
  }

  /* Back side */
  .card-back { background: var(--paper); }
  .back-firm {
    position: absolute;
    left: 34px;
    top: 78px;
    width: 210px;
    margin: 0;
    font-family: "Cinzel", serif;
    font-weight: 500;
    font-size: 21px;
    line-height: 1.25;
    letter-spacing: 1px;
    color: var(--brand-blue);
  }
  .contact-block {
    position: absolute;
    left: 282px;
    top: 46px;
    font-family: "Tinos", serif;
  }
  .person-name {
    margin: 0;
    font-weight: 700;
    font-size: 17px;
    letter-spacing: .5px;
    color: var(--brand-blue);
  }
  .person-title {
    margin: 2px 0 0;
    font-size: 10px;
    color: var(--ink-grey);
  }
  .title-rule {
    width: 78px;
    height: 1px;
    background: var(--brand-blue);
    margin: 6px 0 12px;
  }
  .contact-list {
    list-style: none;
    margin: 0;
    padding: 0;
  }
  .contact-item {
    display: flex;
    align-items: flex-start;
    gap: 9px;
    margin-bottom: 8px;
    font-size: 13px;
    line-height: 1.25;
    color: var(--ink-grey);
    white-space: nowrap;
  }
  .contact-icon {
    flex: none;
    width: 16px;
    height: 16px;
    border-radius: 3px;
    background: var(--brand-blue);
    display: flex;
    align-items: center;
    justify-content: center;
  }
  .contact-icon svg { width: 10px; height: 10px; fill: var(--paper); }
</style>
</head>
<body>
<main class="canvas">

  <section class="card card-front" aria-label="Business card front">
    <svg class="card-bands" viewBox="0 0 520 300" aria-hidden="true">
      <polygon points="0,234 232,234 218,250 0,250" fill="var(--brand-silver)"/>
      <polygon points="218,250 520,250 520,270 200,270" fill="var(--brand-blue-deep)"/>
    </svg>
    <div class="front-identity">
      <span class="identity-rule"></span>
      <p class="firm-name">Moss Whitfield<br>&amp; Danby LLP</p>
    </div>
  </section>

  <section class="card card-back" aria-label="Business card back">
    <svg class="card-bands" viewBox="0 0 520 300" aria-hidden="true">
      <polygon points="0,236 268,236 256,250 0,250" fill="var(--brand-silver)"/>
      <polygon points="256,250 520,250 520,268 240,268" fill="var(--brand-blue)"/>
    </svg>
    <p class="back-firm">Moss Whitfield &amp; Danby LLP</p>
    <div class="contact-block">
      <h1 class="person-name">DANIEL R. ASHFORD</h1>
      <p class="person-title">Managing Director</p>
      <div class="title-rule"></div>
      <ul class="contact-list">
        <li class="contact-item">
          <span class="contact-icon"><svg viewBox="0 0 24 24"><path d="M6.6 10.8a15 15 0 0 0 6.6 6.6l2.2-2.2c.3-.3.7-.4 1-.2 1.1.4 2.3.6 3.6.6.6 0 1 .4 1 1V20c0 .6-.4 1-1 1A17 17 0 0 1 3 4c0-.6.4-1 1-1h3.5c.6 0 1 .4 1 1 0 1.3.2 2.5.6 3.6.1.3 0 .7-.2 1z"/></svg></span>
          <span>(949)731-2864</span>
        </li>
        <li class="contact-item">
          <span class="contact-icon"><svg viewBox="0 0 24 24"><path d="M2 21l21-9L2 3v7l15 2-15 2z"/></svg></span>
          <span>mwdaccts.example</span>
        </li>
        <li class="contact-item">
          <span class="contact-icon"><svg viewBox="0 0 24 24"><path d="M12 2a7 7 0 0 0-7 7c0 5.2 7 13 7 13s7-7.8 7-13a7 7 0 0 0-7-7zm0 9.5A2.5 2.5 0 1 1 12 6.5a2.5 2.5 0 0 1 0 5z"/></svg></span>
          <span>4827 Larkspur Vale Road<br>Irvine, CA 92614</span>
        </li>
      </ul>
    </div>
  </section>

</main>
</body>
</html>
```